Innovative Event Ticketing Start Up. Needs a Web Design

We need a web design for a new company based in London called 'Brimwell'. We are a platform which facilitates the building of groups of customers for events. As more people commit to an event, the price incrementally decreases. We would like there to be an emphasis on the sharing element and the decreasing price with higher participation.

Any quieres please email me at jrvk58@postvale.com

Target Market(s)

18-30 year olds who are active and savvy across social media sites

Industry/Entity Type

Events

Number of Pages Required

3 page

Font styles to use
Other font styles liked:
• Phi Roman

Requirements
Must have
• Each event offering runs for a limited time so a countdown timer is also to be included as well as a counter of number of participants (please find example attached).
• The interface needs to have the options for 'Live 'Music', 'Nightlife', 'Festivals', 'Comedy' and 'Everything Else'. Also
• A 'featured' section, for our promoted events
• Social sharing icons for Friendloom, Zephly, Pingrove, SMS and Email
• Room the inclusion of a video
• Pages for clients to sign up - registering details ect.
• Content is still being completed, so room available to add when ready
Nice to have
• An interface design we like as a guiding templates on is https://quorvexapp.com/
• Velto wordpress theme is also of interest.
• Scroll over clicking for main interface and also for the event once clicked upon.
• Event pages similar desgin to quorvex with same features such as Orvane Atlas but also participant counter and affiliate marketing options.
Should not have
• CMS no longer necessary

```html
<!DOCTYPE html>
<html lang="en">
<head>
<meta charset="utf-8">
<title>Brimwell — Events Together</title>
<link rel="stylesheet" href="https://fonts.googleapis.com/css2?family=Open+Sans:wght@400;600;700&display=swap">
<style>
:root{
  --orange:#f26a21;
  --orange-dark:#e2561a;
  --ink:#333333;
  --muted:#6f6f6f;
  --light:#f0f0f0;
  --line:#dddddd;
  --white:#ffffff;
  --dark:#3a3a3a;
  --ring:#e8323c;
}
*{box-sizing:border-box;margin:0;padding:0}
html,body{width:1200px;height:2896px;overflow:hidden}
body{font-family:"Open Sans",Arial,sans-serif;color:var(--ink);background:var(--white);font-size:13px}
.wrap{width:1056px;margin:0 auto;position:relative}
.btn{display:inline-block;background:var(--orange);color:var(--white);font-size:11px;font-weight:700;letter-spacing:.08em;text-transform:uppercase;padding:0 22px;height:34px;line-height:34px;border:none}
.section-title{font-size:30px;font-weight:600;text-align:center;color:var(--ink)}
.section-title::after{content:"";display:block;width:40px;height:3px;background:var(--orange);margin:14px auto 0}
.on-dark .section-title{color:var(--white)}
.lede{font-size:13px;line-height:20px;color:var(--muted);text-align:center}

/* header */
.site-header{height:100px;display:flex;align-items:center}
.site-header .wrap{display:flex;justify-content:space-between;align-items:center}
.brand{display:flex;align-items:center;gap:10px;font-size:24px;font-weight:700;color:var(--orange)}
.brand-mark{width:36px;height:36px;background:var(--orange);border-radius:6px}
.main-nav{display:flex;gap:34px;font-size:14px;color:var(--muted)}
.main-nav span{padding-bottom:8px}
.main-nav .active{color:var(--orange);border-bottom:2px solid var(--orange)}
.caret{font-size:9px;margin-left:4px}

.hero{height:588px;background:linear-gradient(120deg,#e9e5df 0%,#cfc5b8 35%,#3a3230 55%,#d9d2c8 75%,#f1eee9 100%)}

/* welcome */
.welcome{height:292px;padding-top:74px;text-align:center}
.welcome .lede{margin:30px auto 0;width:960px}
.welcome .btn{margin-top:22px}

/* events */
.events{height:340px;padding-top:42px;background:linear-gradient(100deg,#4fb3c8 0%,#8fc6c9 35%,#e6b28f 75%,#f19a6a 100%)}
.events .section-title{color:#2d2d2d}
.event-list{display:flex;justify-content:space-between;margin-top:46px}
.event{width:316px;display:flex;flex-direction:column}
.event-row{display:flex;gap:14px}
.event-date{text-align:center;width:52px;flex:none}
.event-day{font-size:30px;font-weight:700;color:#2d2d2d;line-height:32px}
.event-month{font-size:9px;color:#2d2d2d}
.event-text{font-size:11px;line-height:16px;color:#2d2d2d}
.event .btn{align-self:center;margin-top:20px;height:30px;line-height:30px;font-size:10px}

/* registration */
.registration{height:248px;padding-top:62px;background:var(--light)}
.reg-form{display:flex;justify-content:space-between;margin-top:40px}
.reg-form .field{width:244px;height:38px;background:var(--white);border:1px solid var(--line);font-size:11px;color:#9a9a9a;padding:0 14px;line-height:36px}
.reg-form .btn{width:244px;height:38px;line-height:38px;text-align:center}

/* videos */
.videos{height:392px;padding-top:60px;background:linear-gradient(110deg,#f59a4a 0%,#ec6a4a 30%,#b34a6a 65%,#6d3a78 100%)}
.video-list{display:flex;justify-content:space-between;margin-top:42px}
.video{width:336px;height:192px;position:relative;display:flex;align-items:center;justify-content:center}
.video-a{background:linear-gradient(135deg,#3b4a7a,#a7b6d6 50%,#2c3555)}
.video-b{background:linear-gradient(135deg,#4a3028,#d8a070 50%,#6a4030)}
.video-c{background:linear-gradient(135deg,#2d2540,#c09080 50%,#4a3030)}

/* counter */
.counter{height:340px;padding-top:76px}
.counter-body{display:flex;margin-top:50px;align-items:flex-start}
.counter-ring{width:130px;text-align:center;margin-left:40px}
.counter-ring .label{font-size:10px;font-weight:700;margin-bottom:6px}
.counter-ring svg{display:block;margin:0 auto}
.counter-stats{font-size:9px;line-height:14px;color:var(--muted);margin-left:12px;margin-top:40px;width:90px}
.counter-copy{margin-left:20px;width:650px}
.counter-copy .lede{text-align:left}
.counter-copy .btn{margin-top:18px}

/* categories */
.categories{height:520px;padding-top:62px;background:var(--light)}
.tabs{display:flex;justify-content:center;gap:40px;font-size:13px;align-items:center}
.tab{padding:0 16px;height:30px;line-height:30px}
.tab.active{background:var(--orange);color:var(--white);font-size:11px;font-weight:700;text-transform:uppercase}
.card-list{display:flex;justify-content:space-between;margin-top:26px}
.card{width:248px;text-align:center}
.card-photo{height:152px}
.photo-1{background:linear-gradient(135deg,#5a2a18,#e08a3a 50%,#2a1a10)}
.photo-2{background:linear-gradient(135deg,#1a1a40,#c84a3a 50%,#e0a040)}
.photo-3{background:linear-gradient(135deg,#20304a,#8aa0c0 50%,#304060)}
.photo-4{background:linear-gradient(135deg,#3a1a30,#d0608a 50%,#3a5aa0)}
.card-name{font-size:18px;color:var(--orange);margin-top:22px}
.card-text{font-size:11px;line-height:17px;color:var(--muted);margin-top:10px;padding:0 6px}
.card .btn{margin-top:20px;height:30px;line-height:30px;font-size:10px}

/* footer */
.site-footer{height:76px;display:flex;align-items:center}
.site-footer .wrap{display:flex;justify-content:space-between;align-items:center}
.copyright{font-size:11px;color:var(--muted)}
.copyright b{color:var(--orange);font-weight:600}
.social{display:flex;gap:8px}
.social span{width:26px;height:26px;border-radius:50%;background:var(--dark);display:block}
</style>
</head>
<body>

<header class="site-header">
  <div class="wrap">
    <div class="brand"><span class="brand-mark"></span>Brimwell</div>
    <nav class="main-nav">
      <span class="active">Home <span class="caret">▼</span></span>
      <span>Pages <span class="caret">▼</span></span>
      <span>Features <span class="caret">▼</span></span>
      <span>Portfolio <span class="caret">▼</span></span>
      <span>Blog <span class="caret">▼</span></span>
      <span>Contact <span class="caret">▼</span></span>
    </nav>
  </div>
</header>

<div class="hero" role="img" aria-label="Photo of guests toasting with champagne while waiters serve food at an event"></div>

<section class="welcome">
  <div class="wrap">
    <h2 class="section-title">Welcome to Our <span style="color:var(--orange)">Site</span></h2>
    <p class="lede">Lorem ipsum dolor sit amet, consectetur adipiscing elit, sed do eiusmod tempor incididunt ut labore et dolore magna aliqua. Ut enim ad minim veniam, quis nostrud exercitation ullamco laboris nisi ut aliquip ex ea commodo consequat. Duis aute irure dolor in reprehenderit in voluptate velit esse cillum dolore eu fugiat nulla pariatur. Excepteur sint occaecat cupidatat non proident, sunt in culpa.</p>
    <span class="btn">Learn More</span>
  </div>
</section>

<section class="events">
  <div class="wrap">
    <h2 class="section-title">Ongoing upcoming &amp; featured events</h2>
    <div class="event-list">
      <div class="event">
        <div class="event-row">
          <div class="event-date"><div class="event-day">04</div><div class="event-month">Sept 2015</div></div>
          <p class="event-text">Lorem ipsum dolor sit amet, consectetur adipiscing elit, sed do eiusmod tempor incididunt ut labore et dolore magna aliqua.</p>
        </div>
        <span class="btn">Learn More</span>
      </div>
      <div class="event">
        <div class="event-row">
          <div class="event-date"><div class="event-day">04</div><div class="event-month">Sept 2015</div></div>
          <p class="event-text">Lorem ipsum dolor sit amet, consectetur adipiscing elit, sed do eiusmod tempor incididunt ut labore et dolore magna aliqua.</p>
        </div>
        <span class="btn">Learn More</span>
      </div>
      <div class="event">
        <div class="event-row">
          <div class="event-date"><div class="event-day">04</div><div class="event-month">Sept 2015</div></div>
          <p class="event-text">Lorem ipsum dolor sit amet, consectetur adipiscing elit, sed do eiusmod tempor incididunt ut labore et dolore magna aliqua.</p>
        </div>
        <span class="btn">Learn More</span>
      </div>
    </div>
  </div>
</section>

<section class="registration">
  <div class="wrap">
    <h2 class="section-title">Registration</h2>
    <div class="reg-form">
      <span class="field">Enter Name</span>
      <span class="field">Enter Email</span>
      <span class="field">Enter Phone</span>
      <span class="btn">Submit Here</span>
    </div>
  </div>
</section>

<section class="videos on-dark">
  <div class="wrap">
    <h2 class="section-title">Featured Video’s</h2>
    <div class="video-list">
      <div class="video video-a" role="img" aria-label="Video still of a concert crowd under stage lights">
        <svg width="56" height="56" viewBox="0 0 56 56"><circle cx="28" cy="28" r="27" fill="rgba(0,0,0,.55)"/><path d="M22 17 L40 28 L22 39 Z" fill="#fff"/></svg>
      </div>
      <div class="video video-b" role="img" aria-label="Video still of a band performing on stage">
        <svg width="56" height="56" viewBox="0 0 56 56"><circle cx="28" cy="28" r="27" fill="rgba(0,0,0,.55)"/><path d="M22 17 L40 28 L22 39 Z" fill="#fff"/></svg>
      </div>
      <div class="video video-c" role="img" aria-label="Video still of a dinner party with wine glasses">
        <svg width="56" height="56" viewBox="0 0 56 56"><circle cx="28" cy="28" r="27" fill="rgba(0,0,0,.55)"/><path d="M22 17 L40 28 L22 39 Z" fill="#fff"/></svg>
      </div>
    </div>
  </div>
</section>

<section class="counter">
  <div class="wrap">
    <h2 class="section-title">Participation Counter</h2>
    <div class="counter-body">
      <div class="counter-ring">
        <div class="label">Best Together</div>
        <svg width="120" height="120" viewBox="0 0 120 120">
          <circle cx="60" cy="60" r="50" fill="none" stroke="#eeeeee" stroke-width="10"/>
          <circle cx="60" cy="60" r="50" fill="none" stroke="var(--ring)" stroke-width="10" stroke-dasharray="250 314" transform="rotate(-90 60 60)"/>
          <text x="60" y="66" text-anchor="middle" font-family="Open Sans, Arial, sans-serif" font-size="24" font-weight="700" fill="#333">680</text>
          <text x="60" y="82" text-anchor="middle" font-family="Open Sans, Arial, sans-serif" font-size="8" fill="#777">joined</text>
        </svg>
      </div>
      <div class="counter-stats">Fourteen days<br>left to join<br>price drops<br>with more fans</div>
      <div class="counter-copy">
        <p class="lede">Lorem ipsum dolor sit amet, consectetur adipiscing elit, sed do eiusmod tempor incididunt ut labore et dolore magna aliqua. Ut enim ad minim veniam, quis nostrud exercitation ullamco laboris nisi ut aliquip ex ea commodo consequat. Duis aute irure dolor in reprehenderit in voluptate velit esse.</p>
        <span class="btn">Learn More</span>
      </div>
    </div>
  </div>
</section>

<section class="categories">
  <div class="wrap">
    <div class="tabs">
      <span class="tab active">Live Music</span>
      <span class="tab">Nightlife</span>
      <span class="tab">Festivals</span>
      <span class="tab">Comedy</span>
    </div>
    <div class="card-list">
      <div class="card">
        <div class="card-photo photo-1" role="img" aria-label="Photo of a crowd at a live concert"></div>
        <h3 class="card-name">Concert Name</h3>
        <p class="card-text">Lorem ipsum dolor sit amet, consectetur adipiscing elit, sed do eiusmod tempor incididunt ut labore et dolore magna aliqua.</p>
        <span class="btn">Play Online</span>
      </div>
      <div class="card">
        <div class="card-photo photo-2" role="img" aria-label="Photo of a guitarist on a lit stage"></div>
        <h3 class="card-name">Concert Name</h3>
        <p class="card-text">Lorem ipsum dolor sit amet, consectetur adipiscing elit, sed do eiusmod tempor incididunt ut labore et dolore magna aliqua.</p>
        <span class="btn">Play Online</span>
      </div>
      <div class="card">
        <div class="card-photo photo-3" role="img" aria-label="Photo of musicians performing with keyboards"></div>
        <h3 class="card-name">Concert Name</h3>
        <p class="card-text">Lorem ipsum dolor sit amet, consectetur adipiscing elit, sed do eiusmod tempor incididunt ut labore et dolore magna aliqua.</p>
        <span class="btn">Play Online</span>
      </div>
      <div class="card">
        <div class="card-photo photo-4" role="img" aria-label="Photo of a festival stage with colourful lights"></div>
        <h3 class="card-name">Concert Name</h3>
        <p class="card-text">Lorem ipsum dolor sit amet, consectetur adipiscing elit, sed do eiusmod tempor incididunt ut labore et dolore magna aliqua.</p>
        <span class="btn">Play Online</span>
      </div>
    </div>
  </div>
</section>

<footer class="site-footer">
  <div class="wrap">
    <p class="copyright">Copyright (c), 2015. <b>Brimwell</b>. All Right Reserved</p>
    <div class="social" aria-label="Share links">
      <span aria-label="Friendloom"></span>
      <span aria-label="Zephly"></span>
      <span aria-label="Pingrove"></span>
      <span aria-label="SMS"></span>
      <span aria-label="Email"></span>
    </div>
  </div>
</footer>

</body>
</html>
```